Flyer Advertisement Simple But Creative

Flyer dimensions 4" x 6"

Simple design with logo and additional info. On the front of the flyer:

- place the logo at the top
- beneath the logo add the website and phone number
- simple less is more approach
- feel free to add your own personal touch

On the back:

- Requirements
- Perfect for Birthdays and Anniversaries
- Rentals available hourly, daily, and weekly
- Group Rentals available at discounted rates
- Enter to win a free rental - url and QR code

Industry/Entity Type

Car Rental

Font styles to use
Serif
Sans Serif

Colors

Designer to choose colors to be used in the design.

Requirements
Must have
• FRONT:
• Please include our phone number and website:
• 614-287-3951
• www.BrindlewoodTrikeHire.example
• BACK:
• REQUIREMENTS
• At least 25 years of age
• Valid Driver's License
• Debit or Credit Card
• Must know how to drive a manual transmission or stick shift

```html
<!DOCTYPE html>
<html lang="en">
<head>
<meta charset="UTF-8">
<title>Trike Hire Flyer – Back</title>
<link href="https://fonts.googleapis.com/css2?family=Marcellus&family=Tenor+Sans&display=swap" rel="stylesheet">
<style>
  :root {
    --paper: #ffffff;
    --berry: #9e0748;
    --hot-pink: #ff1166;
    --mist: #f4f8f8;
    --plum: #4a1535;
    --ink-light: #ffffff;
    --drop: rgba(55, 0, 25, 0.65);
  }
  html, body {
    margin: 0;
    padding: 0;
    width: 800px;
    height: 1200px;
    overflow: hidden;
    background: var(--paper);
  }
  .flyer {
    position: relative;
    width: 800px;
    height: 1200px;
    overflow: hidden;
    background: var(--paper);
    font-family: "Tenor Sans", "Optima", sans-serif;
  }
  .panel {
    position: absolute;
    left: 15px;
    top: 15px;
    width: 773px;
    height: 1166px;
    background: var(--berry);
  }
  .shadowed {
    color: var(--ink-light);
    text-shadow: 7px 13px 6px var(--drop);
  }
  .headline {
    position: absolute;
    left: 0;
    top: 68px;
    width: 800px;
    margin: 0;
    text-align: center;
    font-family: "Marcellus", serif;
    font-weight: 400;
    font-size: 44px;
    line-height: 57px;
    letter-spacing: 1px;
  }
  .rentals-title {
    position: absolute;
    left: 0;
    top: 240px;
    width: 800px;
    margin: 0;
    text-align: center;
    font-size: 29px;
    font-weight: 700;
  }
  .rental-terms {
    position: absolute;
    left: 262px;
    top: 318px;
    margin: 0;
    padding: 0;
    list-style: none;
    font-size: 32px;
    line-height: 40.5px;
  }
  .rental-terms li::before {
    content: "•";
    display: inline-block;
    width: 53px;
    font-size: 26px;
  }
  .group-offer {
    position: absolute;
    left: 0;
    top: 521px;
    width: 800px;
    margin: 0;
    text-align: center;
    font-size: 32px;
    line-height: 40px;
  }
  .giveaway {
    position: absolute;
    left: 93px;
    top: 657px;
    margin: 0;
    font-size: 32px;
    line-height: 40px;
  }
  .requirements {
    position: absolute;
    left: 131px;
    top: 778px;
    width: 516px;
    height: 516px;
    border-radius: 50%;
    border: 11px solid var(--hot-pink);
    background: var(--mist);
    box-shadow: 12px 18px 14px rgba(30, 0, 15, 0.75);
    color: var(--plum);
    text-align: center;
  }
  .requirements h2 {
    margin: 64px 0 0;
    font-size: 31px;
    font-weight: 700;
    letter-spacing: 1px;
  }
  .requirements ul {
    margin: 22px 0 0;
    padding: 0;
    list-style: none;
    font-size: 31px;
    line-height: 40px;
  }
  .requirements li.narrow {
    padding: 0 60px;
  }
</style>
</head>
<body>
<main class="flyer">
  <div class="panel"></div>

  <h1 class="headline shadowed">PERFECT FOR BIRTHDAYS<br>AND ANNIVERSARIES!</h1>

  <p class="rentals-title shadowed">Rentals available:</p>
  <ul class="rental-terms shadowed">
    <li>Hourly</li>
    <li>Daily</li>
    <li>Weekly</li>
  </ul>

  <p class="group-offer shadowed">Group Rentals available at discounted<br>rates</p>

  <p class="giveaway shadowed">Enter to win a free rental - url and QR</p>

  <section class="requirements">
    <h2>REQUIREMENTS:</h2>
    <ul>
      <li>At least 25 years of age</li>
      <li>Valid Driver’s License</li>
      <li>Debit or Credit Card</li>
      <li class="narrow">Must know how to drive a manual transmission or stick shift</li>
    </ul>
  </section>
</main>
</body>
</html>
```